Frostvale Climate Crew WA Truck

I want a truck desing that screams Professional, Friendly and serious about work. you can find some of our work on our website, facebook and instagram.
https://breezelinecrew.example.com.au/
https://www.instagram.com/bzcrewox/
https://www.facebook.com/profile.php?id=70318825094631

The design needs to include our refrigeration license: AU38452 and electrical License: EC94031
I want the colours to be consistent with my Logo.

Key Notes to be included in the design, I want to let people know we do the following;
- Commercial and Residential
- Repairs, Service and Installation
- Reverse cycle ducted Air Conditioning
- Wall Split Air Conditioning
- Ceiling Cassettes
- Evaporative Air Conditioning
- Cool Rooms
- Display Fridges
- Beer Chillers

```html
<!DOCTYPE html>
<html lang="en">
<head>
<meta charset="utf-8">
<title>Frostvale Climate Crew WA – Truck Livery</title>
<link href="https://fonts.googleapis.com/css2?family=Audiowide&family=Exo+2:wght@500;700&family=Michroma&display=swap" rel="stylesheet">
<style>
  :root {
    --navy: #0b2f63;
    --blue: #15569a;
    --orange: #f2a023;
    --red: #e0451b;
    --paper: #f7f7f7;
    --ink: #0e2a55;
    --white: #ffffff;
    --frame: #b9bcc0;
  }
  html, body { margin: 0; padding: 0; overflow: hidden; }
  body {
    width: 1200px; height: 1200px; background: var(--white);
    position: relative; font-family: "Exo 2", sans-serif;
  }
  .panel { position: absolute; background: var(--paper); overflow: hidden; outline: 3px solid var(--frame); }
  .panel svg.backdrop { position: absolute; inset: 0; }
  .side-panel { left: 50px; top: 40px; width: 1100px; height: 530px; }
  .rear-panel { left: 300px; top: 625px; width: 600px; height: 540px; }

  .brand { position: absolute; display: flex; flex-direction: column; align-items: center; text-align: center; }
  .brand-dot { border-radius: 50%; background: var(--blue); flex: none; }
  .brand-name { font-family: "Exo 2", sans-serif; font-weight: 700; color: var(--red); line-height: 1.1; }

  .website { position: absolute; font-family: "Michroma", sans-serif; color: var(--ink); white-space: nowrap; text-align: center; }

  .services { position: absolute; margin: 0; padding: 0; list-style: none; font-weight: 500; }
  .services li { position: relative; padding-left: 18px; }
  .services li::before {
    content: ""; position: absolute; left: 0; border-radius: 50%; background: var(--orange);
  }

  .call { position: absolute; display: flex; align-items: center; gap: 10px; }
  .call-label { font-family: "Audiowide", sans-serif; color: var(--orange); white-space: nowrap; }
  .phone-number { position: absolute; font-family: "Audiowide", sans-serif; color: var(--white); white-space: nowrap; }
  .licences { position: absolute; color: var(--white); font-weight: 500; text-align: center; line-height: 1.15; }

  /* side */
  .side-panel .brand { left: 62px; top: 70px; width: 400px; gap: 16px; }
  .side-panel .brand-dot { width: 90px; height: 90px; }
  .side-panel .brand-name { font-size: 38px; }
  .side-panel .website { left: 62px; top: 378px; width: 400px; font-size: 15px; }
  .side-panel .services { left: 698px; top: 100px; color: var(--white); font-size: 19.5px; }
  .side-panel .services li { height: 32.5px; }
  .side-panel .services li::before { width: 11px; height: 11px; top: 8px; }
  .side-panel .call { left: 512px; top: 415px; }
  .side-panel .call-label { font-size: 30px; }
  .side-panel .phone-number { left: 448px; top: 472px; font-size: 38px; letter-spacing: 1px; }
  .side-panel .licences { left: 900px; top: 440px; font-size: 24px; width: 150px; }

  /* rear */
  .rear-panel .brand { left: 10px; top: 60px; width: 270px; gap: 10px; }
  .rear-panel .brand-dot { width: 54px; height: 54px; }
  .rear-panel .brand-name { font-size: 22px; }
  .rear-panel .website { left: 10px; top: 218px; width: 270px; font-size: 9.3px; }
  .rear-panel .services { left: 345px; top: 20px; color: var(--ink); font-size: 13.5px; width: 215px; }
  .rear-panel .services li { line-height: 25px; padding-left: 13px; }
  .rear-panel .services li::before { width: 7px; height: 7px; top: 9px; }
  .rear-panel .call { left: 14px; top: 360px; gap: 8px; }
  .rear-panel .call-label { font-size: 22px; }
  .rear-panel .phone-number { left: 20px; top: 398px; font-size: 22px; letter-spacing: 1px; }
  .rear-panel .licences { left: 370px; top: 485px; font-size: 20px; width: 130px; }
  .door-seam { position: absolute; left: 296px; top: 0; width: 8px; height: 540px; background: var(--frame); }
</style>
</head>
<body>

<section class="panel side-panel" aria-label="Truck side panel">
  <svg class="backdrop" width="1100" height="530" viewBox="0 0 1100 530" aria-hidden="true">
    <defs>
      <linearGradient id="sideBlue" x1="0" y1="0" x2="0" y2="1">
        <stop offset="0" stop-color="#1a5ea6"/><stop offset="1" stop-color="#0a2c5e"/>
      </linearGradient>
      <linearGradient id="sideSwoosh" x1="0" y1="0" x2="0" y2="1">
        <stop offset="0" stop-color="#f4a623"/><stop offset="1" stop-color="#e0401a"/>
      </linearGradient>
    </defs>
    <path d="M600,0 C645,260 470,460 230,530 L300,530 C505,455 655,250 650,0 Z" fill="url(#sideSwoosh)"/>
    <path d="M665,0 C668,250 510,460 318,530 L1100,530 L1100,0 Z" fill="url(#sideBlue)"/>
  </svg>

  <div class="brand">
    <span class="brand-dot"></span>
    <span class="brand-name">Frostvale Climate<br>Crew WA</span>
  </div>
  <div class="website">frostvalecrew.example.com.au</div>

  <ul class="services">
    <li>Commercial and Residential</li>
    <li>Repairs, Service and Installation</li>
    <li>Reverse cycle ducted Air Conditioning</li>
    <li>Wall Split Air Conditioning</li>
    <li>Ceiling Cassettes</li>
    <li>Evaporative Air Conditioning</li>
    <li>Cool Rooms</li>
    <li>Display Fridges</li>
    <li>Beer Chillers</li>
  </ul>

  <div class="call">
    <svg width="48" height="48" viewBox="0 0 48 48" aria-hidden="true">
      <circle cx="24" cy="24" r="23" fill="var(--orange)"/>
      <path d="M16 13 l5 0 l2 7 l-3 2 a16 16 0 0 0 8 8 l2 -3 l7 2 l0 5 a3 3 0 0 1 -3 3 a22 22 0 0 1 -21 -21 a3 3 0 0 1 3 -3 Z" fill="var(--white)"/>
    </svg>
    <span class="call-label">CALL NOW!</span>
  </div>
  <div class="phone-number">234-555-0147</div>
  <div class="licences">AU38452<br>EC94031</div>
</section>

<section class="panel rear-panel" aria-label="Truck rear doors">
  <svg class="backdrop" width="600" height="540" viewBox="0 0 600 540" aria-hidden="true">
    <defs>
      <linearGradient id="rearBlue" x1="0" y1="0" x2="0" y2="1">
        <stop offset="0" stop-color="#1a5ea6"/><stop offset="1" stop-color="#0a2c5e"/>
      </linearGradient>
      <linearGradient id="rearSwoosh" x1="0" y1="0" x2="1" y2="0">
        <stop offset="0" stop-color="#e0401a"/><stop offset="0.5" stop-color="#f4a623"/><stop offset="1" stop-color="#f2a023"/>
      </linearGradient>
    </defs>
    <path d="M0,255 Q300,425 600,215 L600,250 Q300,455 0,290 Z" fill="url(#rearSwoosh)"/>
    <path d="M0,300 Q300,470 600,262 L600,540 L0,540 Z" fill="url(#rearBlue)"/>
  </svg>
  <div class="door-seam"></div>

  <div class="brand">
    <span class="brand-dot"></span>
    <span class="brand-name">Frostvale Climate<br>Crew WA</span>
  </div>
  <div class="website">frostvalecrew.example.com.au</div>

  <ul class="services">
    <li>Commercial and Residential</li>
    <li>Repairs, Service and Installation</li>
    <li>Reverse cycle ducted Air Conditioning</li>
    <li>Wall Split Air Conditioning</li>
    <li>Ceiling Cassettes</li>
    <li>Evaporative Air Conditioning</li>
    <li>Cool Rooms</li>
    <li>Display Fridges</li>
    <li>Beer Chillers</li>
  </ul>

  <div class="call">
    <svg width="36" height="36" viewBox="0 0 48 48" aria-hidden="true">
      <circle cx="24" cy="24" r="23" fill="var(--orange)"/>
      <path d="M16 13 l5 0 l2 7 l-3 2 a16 16 0 0 0 8 8 l2 -3 l7 2 l0 5 a3 3 0 0 1 -3 3 a22 22 0 0 1 -21 -21 a3 3 0 0 1 3 -3 Z" fill="var(--white)"/>
    </svg>
    <span class="call-label">CALL NOW!</span>
  </div>
  <div class="phone-number">234-555-0147</div>
  <div class="licences">AU38452<br>EC94031</div>
</section>

</body>
</html>
```